Online trading school - Website design

We are building an online trading school (trading of shares, commodities, indices, currencies). The purpose is to teach online traders how to trade successfully. We need to design the homepage of the website and logo (bramwelloq.com will be the domain). The homepage will contain the following elements

- logo
- Sign in and Register links/buttons
- upper menu
- short introduction
- a couple of bullet points 'Why to join our school?'
- sign up form
- text
- bottom menu

Attached is a draft for the designer. The draft is just for an inspiration, the actual structure of the website can be different if the designer thinks so.

The designer is free to choose colors.

School

3 page

```html
<!DOCTYPE html>
<html lang="en">
<head>
<meta charset="utf-8">
<title>Bramwelloq – Online Trading School</title>
<link href="https://fonts.googleapis.com/css2?family=Anton&family=Oswald:wght@500&family=Open+Sans:ital,wght@0,400;0,600;0,700;0,800;1,400&display=swap" rel="stylesheet">
<style>
:root{
  --blue:#1ea7e1;
  --blue-dark:#0a8fd0;
  --ink:#1b1b1b;
  --text:#333;
  --muted:#888;
  --band:#ebebeb;
  --orange:#f5a300;
  --red:#d90f0f;
  --white:#fff;
}
*{box-sizing:border-box;margin:0;padding:0}
html,body{width:888px;height:1200px;overflow:hidden;background:var(--white)}
body{position:relative;font-family:"Open Sans",sans-serif;color:var(--text)}
.abs{position:absolute}

.brand{left:166px;top:15px;display:flex;align-items:center;gap:8px}
.brand-mark{width:12px;height:12px;background:var(--blue)}
.brand-name{font-family:"Open Sans",sans-serif;font-weight:700;font-size:19px;color:var(--ink)}

.social{top:22px;left:555px;display:flex;gap:5px}
.social span{width:11px;height:11px;display:block}
.btn-top{top:21px;height:15px;font-size:6.5px;font-weight:700;color:#fff;display:flex;align-items:center;justify-content:center;letter-spacing:.3px}
.btn-signin{left:603px;width:47px;background:var(--blue-dark)}
.btn-register{left:657px;width:46px;background:#3cb9ec}

.nav{top:54px;left:0;width:888px;height:31px;background:var(--band)}
.nav a{position:absolute;top:11px;font-size:7px;color:#666;text-decoration:none;letter-spacing:.2px}
.nav a.active{color:var(--blue)}

.hero{top:85px;left:0;width:888px;height:248px;background:radial-gradient(ellipse at 30% 50%,#6a6fb0 0%,#8e8dc4 35%,#b7b3d7 70%,#d8d1e6 100%)}
.hero-photo{top:104px;left:190px;width:170px;height:230px;border-radius:18px;background:linear-gradient(160deg,#2c4fa8,#1c3474)}
.chevron{top:314px;left:436px}

.signup{top:109px;left:546px;width:158px;height:200px;background:#fff;border-top:4px solid var(--blue)}
.signup h2{position:absolute;top:12px;left:0;width:100%;text-align:center;font-family:"Anton",sans-serif;font-weight:400;font-size:14px;color:var(--ink);letter-spacing:.3px}
.signup p{position:absolute;top:38px;left:14px;width:132px;font-size:5.6px;line-height:7.4px;color:#888;text-align:center}
.field{position:absolute;left:12px;width:135px;height:20px;border:1px solid #ddd;background:#f4f4f4;font-size:6px;font-style:italic;color:#aaa;padding:6px 6px}
.agree{position:absolute;top:144px;left:12px;font-size:6px;color:#555;display:flex;align-items:center;gap:6px}
.agree i{width:7px;height:7px;border:1px solid #bbb;display:block;background:#f4f4f4}
.submit{position:absolute;left:0;bottom:0;width:100%;height:40px;background:linear-gradient(#1fb2ee,#0898d8);color:#fff;font-weight:800;font-size:13px;display:flex;align-items:center;justify-content:center;letter-spacing:.5px}

.title{font-family:"Anton",sans-serif;font-weight:400;color:var(--ink);text-align:center;width:888px;left:0;font-size:20px;letter-spacing:.2px}
.intro{top:390px;left:212px;width:465px;font-size:6.5px;line-height:9.7px;text-align:center;color:#333}

.why-band{top:495px;left:0;width:888px;height:230px;background:linear-gradient(#e6e6e6,#f7f7f7 60%,#ececec)}
.why-art{top:518px;left:175px;width:265px;height:207px;background:radial-gradient(circle at 55% 45%,#e9eef5,#f4f4f4 70%);border-radius:10px}
.why-title{top:528px;left:467px;font-family:"Anton",sans-serif;font-weight:400;font-size:19px;color:var(--blue);letter-spacing:.3px}
.why-list{top:567px;left:467px;list-style:none}
.why-list li{font-size:7.6px;font-style:italic;font-weight:400;color:#222;height:14.2px;display:flex;align-items:center;gap:7px}
.why-list li::before{content:"";width:5px;height:5px;border:1.2px solid #222;border-radius:50%}
.btn-red{top:668px;left:467px;width:87px;height:20px;background:var(--red);color:#fff;font-size:7.4px;font-weight:700;display:flex;align-items:center;justify-content:center;letter-spacing:.3px}

.subtitle{top:784px;left:0;width:888px;text-align:center;font-family:"Oswald",sans-serif;font-weight:500;font-size:8.5px;color:var(--muted);letter-spacing:.1px}

.feature-band{top:817px;left:184px;width:520px;height:160px;background:linear-gradient(#e8e8e8,#fff 70%)}
.photo{border:3px solid #ddd}
.photo-1{top:848px;left:215px;width:155px;height:114px;background:linear-gradient(135deg,#1d3f6e,#3d8fc8 60%,#162c52)}
.photo-2{top:1003px;left:520px;width:155px;height:115px;background:linear-gradient(135deg,#4a7cb0,#9fc4e2 55%,#2c5a8a)}
.feat-h{font-family:"Oswald",sans-serif;font-weight:500;font-size:14px;color:var(--orange);text-align:center;transform:skewX(-10deg)}
.feat-p{font-size:6.5px;line-height:9.7px;text-align:center;color:#333}

.footer{top:1147px;left:0;width:888px;height:53px;background:var(--band)}
.footer .copy{position:absolute;top:21px;left:186px;font-size:7px;color:#333}
.footer .links{position:absolute;top:21px;right:183px;font-size:7px;color:var(--blue)}
.footer .links span{margin:0 10px}
</style>
</head>
<body>

<header>
  <div class="abs brand"><span class="brand-mark"></span><span class="brand-name">Bramwelloq</span></div>
  <div class="abs social" aria-label="Social links">
    <span style="background:#3b5a9a"></span><span style="background:#2aa3e0"></span><span style="background:#dd4b39"></span>
  </div>
  <div class="abs btn-top btn-signin">SIGN IN</div>
  <div class="abs btn-top btn-register">REGISTER</div>
</header>

<nav class="abs nav">
  <a class="active" style="left:185px">HOME</a>
  <a style="left:238px">ABOUT OUR SCHOOL</a>
  <a style="left:345px">RISK WARNING</a>
  <a style="left:430px">TRADING GLOSSARY</a>
  <a style="left:532px">SERVICES</a>
  <a style="left:599px">FEATURES</a>
  <a style="left:669px">CONTACT</a>
</nav>

<section class="abs hero" role="img" aria-label="Hand holding a smartphone showing a trading app, blurred background"></section>
<div class="abs hero-photo" role="img" aria-label="Smartphone with trading charts"></div>
<svg class="abs chevron" width="16" height="10" viewBox="0 0 16 10"><path d="M1 1l7 7 7-7" fill="none" stroke="#fff" stroke-width="1.2"/></svg>

<form class="abs signup">
  <h2>JOIN OUR SCHOOL NOW!</h2>
  <p>Ed do eiusmod tempor incididunt ut labor et dolore magna aliqua. Ut enim ad minim</p>
  <div class="field" style="top:60px">First Name</div>
  <div class="field" style="top:87px">LastName</div>
  <div class="field" style="top:114px">Email</div>
  <div class="agree"><i></i>Agree with our terms and Conditions</div>
  <div class="submit">SUBMIT</div>
</form>

<h1 class="abs title" style="top:355px">OCCAECAT CUPIDATAT</h1>
<p class="abs intro">Lorem ipsum dolor sit amet, consectetur adipiscing elit, sed do eiusmod tempor incididunt ut labore et dolore magna aliqua. Ut enim ad minim veniam, quis nostrud exercitation ullamco laboris nisi ut aliquip ex ea commodo consequat. Duis aute irure dolor in reprehenderit in voluptate velit esse cillum dolore eu fugiat nulla pariatur. Excepteur sint occaecat cupidatat non proident, sunt in culpa qui officia deserunt mollit anim id est laborum.Lorem ipsum dolor sit amet, consectetur adipiscing elit, sed do eiusmod tempor incididunt ut labore et dolore magna aliqua. Ut enim ad minim veniam, quis nostrud exercitation ullamco laboris nisi ut aliquip ex ea commodo consequat. Duis aute irure dolor in reprehenderit in voluptate velit esse cillum dolore eu fugiat nulla pariatur. Excepteur sint occaecat cupidatat non proident, sunt in culpa qui officia deserunt mollit anim id est laborum.Lorem ipsum dolor sit amet, consectetur adipiscing elit, sed do eiusmod tempor incididunt ut labore et dolore magna aliqua. Ut enim ad minim veniam, quis nostrud exercitation ullamco</p>

<section class="abs why-band"></section>
<div class="abs why-art" role="img" aria-label="Head silhouette with gears connected to a network of colourful app icons"></div>
<h2 class="abs why-title">WHY TO JOIN US ?</h2>
<ul class="abs why-list">
  <li>Lorem ipsum dolor sit amet, consectetur</li>
  <li>Adipiscing elit, sed do eiusmod tempor</li>
  <li>Ut labore et dolore magna aliqua.</li>
  <li>Ut enim ad minim veniam, quis nostrud</li>
  <li>Exercitation ullamco laboris nisi ut aliquip</li>
  <li>Ex ea commodo consequat.</li>
</ul>
<div class="abs btn-red">EXERCITATION</div>

<h2 class="abs title" style="top:749px">DESERUNT MOLLIT ANIM</h2>
<p class="abs subtitle">QUIS NOSTRUD EXERCITATION ULLAMCO LABORIS NISI UT ALIQUIP</p>

<div class="abs feature-band"></div>
<div class="abs photo photo-1" role="img" aria-label="Businessman with rising financial chart overlay"></div>
<h3 class="abs feat-h" style="top:860px;left:400px;width:275px">CONSECTETUR ADIPISCING ELIT</h3>
<p class="abs feat-p" style="top:888px;left:400px;width:275px">Lorem ipsum dolor sit amet, consectetur adipiscing elit, sed do eiusmod tempor incididunt ut labore et dolore magna aliqua. Ut enim ad minim veniam, quis nostrud exercitation ullamco laboris nisi ut aliquip ex ea commodo consequat. Duis aute irure dolor in reprehenderit in voluptate velit esse cillum dolore eu fugiat nulla pariatur. Excepteur sint occaecat cupidatat non proident, sunt in culpa qui officia deserunt mollit anim id est laborum</p>

<h3 class="abs feat-h" style="top:1015px;left:212px;width:276px">CONSECTETUR ADIPISCING ELIT</h3>
<p class="abs feat-p" style="top:1043px;left:212px;width:276px">Lorem ipsum dolor sit amet, consectetur adipiscing elit, sed do eiusmod tempor incididunt ut labore et dolore magna aliqua. Ut enim ad minim veniam, quis nostrud exercitation ullamco laboris nisi ut aliquip ex ea commodo consequat. Duis aute irure dolor in reprehenderit in voluptate velit esse cillum dolore eu fugiat nulla pariatur. Excepteur sint occaecat cupidatat non proident, sunt in culpa qui officia deserunt mollit anim id est laborum</p>
<div class="abs photo photo-2" role="img" aria-label="Hand touching a digital network interface"></div>

<footer class="abs footer">
  <div class="copy">Copyright © 2016 Bramwelloq All rights reserved.</div>
  <div class="links">Terms and Conditions<span>/</span>Privacy protection</div>
</footer>

</body>
</html>
```